" Somos uma empresa especialista no ramos da engenharia elétrica no que tange a quadros elétricos. Atendemos empresas de engenharia, construção civil, industria, comercio, empreiteiras, engenheiros e técnicos eletricistas, além de revendas de materiais eletricos. Recebemos consultas através da nossa HOME PAGE, E MAIL , TELEFONE e PRESENCIAL. Somos especialistas em materiais específicos para aplicação em toda gama de quadros elétricos e automação e monitoramento de sistemas de energia elétrica. Recebemos o Projeto do cliente e executamos a montagem dos quadros. "

```html
<!DOCTYPE html>
<html lang="pt-BR">
<head>
<meta charset="utf-8">
<title>Vieira Lemos — Quadros Elétricos</title>
<link href="https://fonts.googleapis.com/css2?family=Oswald:wght@400;500&family=Titillium+Web:wght@400;600;700&display=swap" rel="stylesheet">
<style>
:root{
  --ink:#1d1c21;
  --ink-2:#2a2930;
  --yellow:#f4c21b;
  --white:#ffffff;
  --muted:#b9b7c0;
  --brick-a:#3a2a22;
  --brick-b:#1c1512;
}
*{box-sizing:border-box;margin:0;padding:0}
html,body{width:1200px;height:1200px;overflow:hidden;background:var(--ink)}
body{position:relative;font-family:"Titillium Web",sans-serif;color:var(--white)}
.abs{position:absolute}

/* header */
.header{left:0;top:0;width:1200px;height:115px;background:var(--ink)}
.brand{left:132px;top:0;width:212px;height:115px;background:var(--white);display:flex;flex-direction:column;align-items:center;justify-content:center;gap:6px}
.brand-mark{width:30px;height:30px;border-radius:50%;background:var(--ink)}
.brand-name{font-weight:600;font-size:19px;letter-spacing:2px;color:var(--ink);text-transform:uppercase}
.brand-tag{font-size:8px;color:#777;letter-spacing:1px;text-transform:uppercase}
.nav{left:486px;top:28px;display:flex;gap:16px;font-family:"Oswald",sans-serif;font-size:19px;text-transform:uppercase}
.nav a{color:var(--white);text-decoration:none}
.nav a.active{color:var(--yellow)}
.social{left:984px;top:30px;display:flex;gap:22px}
.social span{width:16px;height:16px;background:var(--yellow);display:block}
.contact{top:78px;display:flex;gap:8px;align-items:center;font-size:11px;line-height:1.1;white-space:nowrap}
.contact i{width:12px;height:12px;border:2px solid var(--yellow);border-radius:50%;display:block}
.contact small{display:block;color:var(--muted);font-size:8px}
.tools{left:1108px;top:80px;display:flex;gap:26px}

/* hero */
.hero{left:0;top:115px;width:1200px;height:420px;
  background:
    radial-gradient(ellipse 30% 45% at 18% 35%,rgba(40,40,44,.55),transparent 70%),
    radial-gradient(ellipse 35% 40% at 78% 55%,rgba(150,60,50,.35),transparent 70%),
    radial-gradient(ellipse 25% 30% at 88% 80%,rgba(60,80,140,.35),transparent 70%),
    linear-gradient(115deg,#e6e7e8 0%,#c4c8cb 35%,#8e959b 60%,#b5babe 80%,#6c7379 100%)}
.arrow{top:250px}
.headline{left:82px;top:340px;height:64px;padding:0 24px;background:var(--yellow);display:flex;align-items:center;font-weight:700;font-size:30px;color:var(--ink)}
.cta{left:82px;top:420px;width:172px;height:50px;background:var(--ink);border-left:4px solid var(--yellow);display:flex;align-items:center;justify-content:space-between;padding:0 18px;font-size:19px;font-weight:600}

/* feature strip */
.bricks{left:0;top:535px;width:1200px;height:665px;background:radial-gradient(ellipse at 50% 20%,var(--brick-a),var(--brick-b) 70%)}
.features{left:150px;top:515px;width:900px;height:145px}
.feature{position:absolute;top:14px;width:260px;display:flex;gap:16px}
.feature h3{font-size:17px;line-height:1.1;font-weight:700;text-transform:uppercase;margin-bottom:6px}
.feature p{font-size:12px;line-height:1.25;color:var(--muted)}
.f1 h3{color:var(--yellow)}

/* products */
.section-title{left:0;top:690px;width:1200px;text-align:center;font-weight:700;font-size:38px}
.section-title em{font-style:normal;color:var(--yellow)}
.rule{left:582px;top:745px;width:36px;height:3px;background:var(--white)}
.frame{left:96px;top:772px;width:1010px;height:362px;border:10px solid var(--yellow);background:#f1f1f1}
.tile{position:absolute}
.t-gerais{background:radial-gradient(ellipse 30% 55% at 30% 45%,#f4f5f5,transparent 70%),radial-gradient(ellipse 25% 55% at 72% 45%,#c9ced2,transparent 70%),linear-gradient(160deg,#e9ebec,#9ea4a9)}
.t-especiais{background:radial-gradient(ellipse 35% 60% at 35% 45%,#9aa3ab,transparent 70%),radial-gradient(ellipse 25% 45% at 78% 55%,#b6bcc1,transparent 70%),linear-gradient(160deg,#eeeff0,#c2c6ca)}
.t-controle{background:radial-gradient(ellipse 40% 60% at 25% 45%,#d3d6d9,transparent 70%),radial-gradient(ellipse 30% 55% at 75% 40%,#7f868c,transparent 70%),linear-gradient(160deg,#cfd2d5,#8f969c)}
.t-caixa{background:radial-gradient(ellipse 45% 55% at 50% 45%,#e3e5e7,transparent 70%),linear-gradient(160deg,#f2f3f4,#a9aeb2)}
.t-quadros{background:radial-gradient(ellipse 28% 42% at 35% 55%,#b9bec2,transparent 70%),radial-gradient(ellipse 18% 25% at 78% 62%,#d6d9dc,transparent 70%),linear-gradient(160deg,#f6f6f7,#dfe2e4)}
.label{position:absolute;left:0;right:0;height:28px;background:var(--ink);color:var(--yellow);font-weight:700;font-size:16px;text-transform:uppercase;display:flex;align-items:center;justify-content:center;letter-spacing:1px}
.dots{left:562px;top:1160px;display:flex;gap:8px}
.dots span{width:9px;height:9px;border-radius:50%;background:var(--white)}
.dots span.on{background:var(--yellow)}
</style>
</head>
<body>

<header class="abs header">
  <div class="abs brand"><span class="brand-mark"></span><span class="brand-name">Vieira Lemos</span><span class="brand-tag">Quadros e automação industrial</span></div>
  <nav class="abs nav"><a class="active">Home</a><a>Empresas</a><a>Produtos</a><a>Serviços</a><a>Cases</a><a>Contato</a></nav>
  <div class="abs social"><span></span><span></span><span></span><span></span><span></span></div>
  <div class="abs contact" style="left:770px"><i></i><div>Suporte<small>Fale conosco</small></div></div>
  <div class="abs contact" style="left:870px"><i></i><div>Horário<small>Seg a Sex</small></div></div>
  <div class="abs contact" style="left:966px"><i></i><div>E-mail<small>contato@vlemos.com.br</small></div></div>
  <div class="abs tools">
    <svg width="18" height="18" viewBox="0 0 18 18"><circle cx="7.5" cy="7.5" r="5.5" fill="none" stroke="#fff" stroke-width="2"/><line x1="11.5" y1="11.5" x2="16" y2="16" stroke="#fff" stroke-width="2"/></svg>
    <svg width="18" height="16" viewBox="0 0 18 16"><rect y="1" width="18" height="2" fill="#fff"/><rect y="7" width="18" height="2" fill="#fff"/><rect y="13" width="18" height="2" fill="#fff"/></svg>
  </div>
</header>

<div class="abs hero" role="img" aria-label="Foto de quadro elétrico aberto com disjuntores, relés e fiação colorida"></div>
<svg class="abs arrow" style="left:6px" width="40" height="40" viewBox="0 0 40 40"><path d="M22 6 8 20l14 14M34 6 20 20l14 14" fill="none" stroke="#fff" stroke-width="5"/></svg>
<svg class="abs arrow" style="left:1154px" width="40" height="40" viewBox="0 0 40 40"><path d="M18 6l14 14-14 14M6 6l14 14L6 34" fill="none" stroke="#fff" stroke-width="5"/></svg>
<div class="abs headline">Especialistas em automação e quadros elétricos</div>
<div class="abs cta">Saiba mais <svg width="12" height="18" viewBox="0 0 12 18"><path d="M2 2l8 7-8 7" fill="none" stroke="#fff" stroke-width="3"/></svg></div>

<div class="abs bricks" role="img" aria-label="Fundo de parede de tijolos escuros com iluminação suave"></div>

<div class="abs features">
  <svg class="abs" width="900" height="145" viewBox="0 0 900 145"><polygon points="0,0 900,0 885,125 450,145 15,125" fill="#1d1c21"/><line x1="300" y1="20" x2="300" y2="115" stroke="#3a3941"/><line x1="600" y1="20" x2="600" y2="115" stroke="#3a3941"/></svg>
  <div class="feature f1" style="left:26px">
    <svg width="36" height="44" viewBox="0 0 36 44"><rect x="2" y="2" width="32" height="40" fill="none" stroke="#f4c21b" stroke-width="2"/><rect x="10" y="12" width="16" height="8" fill="none" stroke="#f4c21b" stroke-width="2"/></svg>
    <div><h3>Painéis<br>gerais</h3><p>Painéis desenvolvidos e projetados de acordo com as necessidades dos seus clientes</p></div>
  </div>
  <div class="feature" style="left:320px">
    <svg width="40" height="30" viewBox="0 0 40 30"><rect x="1" y="1" width="38" height="28" fill="none" stroke="#f4c21b" stroke-width="2"/><path d="M6 8h28M6 15h28M6 22h28" stroke="#f4c21b" stroke-width="2"/></svg>
    <div><h3>Controle e<br>automação</h3><p>Totalmente modulares, permitindo o controle completamente centralizado.</p></div>
  </div>
  <div class="feature" style="left:624px">
    <svg width="30" height="44" viewBox="0 0 30 44"><rect x="2" y="2" width="26" height="40" fill="none" stroke="#f4c21b" stroke-width="2"/><line x1="15" y1="2" x2="15" y2="42" stroke="#f4c21b" stroke-width="2"/></svg>
    <div><h3>Caixas e<br>painéis</h3><p>Caixas e painéis vazios, para montadora de painéis, fabricantes de máquinas e outras empresas em geral.</p></div>
  </div>
</div>

<h2 class="abs section-title">Nossos <em>Produtos</em></h2>
<div class="abs rule"></div>

<section class="abs frame">
  <div class="tile t-gerais" style="left:8px;top:8px;width:330px;height:158px" role="img" aria-label="Foto de painéis gerais"><div class="label" style="bottom:0">Painéis gerais</div></div>
  <div class="tile t-especiais" style="left:346px;top:8px;width:250px;height:158px" role="img" aria-label="Foto de painéis especiais"><div class="label" style="bottom:0">Painéis especiais</div></div>
  <div class="tile t-controle" style="left:8px;top:174px;width:400px;height:160px" role="img" aria-label="Foto de painéis de controle e automação"><div class="label" style="bottom:0">Controle e automação</div></div>
  <div class="tile t-caixa" style="left:416px;top:174px;width:180px;height:160px" role="img" aria-label="Foto de caixas de painel vazias"><div class="label" style="bottom:0">Painéis de caixa</div></div>
  <div class="tile t-quadros" style="left:604px;top:8px;width:386px;height:326px" role="img" aria-label="Foto de quadros de distribuição"><div class="label" style="top:0">Quadros de distribuição</div></div>
</section>

<div class="abs dots"><span class="on"></span><span></span><span></span><span></span><span></span></div>

</body>
</html>
```